(front)
BrightCove Logo
Keeping You Competitive
In the ever-changing world of healthcare, you need a partner who can keep you current and ensure you are getting the most out of your rehabilitation services.
(Inside cover)
Our Mission
Quality-Recruitment, management, continued education, research and technology
Compliance-Accuracy of service within practice guidelines and federal regulations
Expertise-Audit and compliance, out-patient, clinical programs, education and career development, evidence based practice and speech and dysphagia programs
Ethics-Integrity and social responsiblity
Vision-Top set the standard of performance and practice within the rehabilitation industry
We're here to help!
-Improve efficiencies
-Optimize outcomes
-Audit for compliance
(Inside Back Cover)
BrightCove Therapy Logo
brightcovetherapy.example
Keeping You Competitive
Call Us Today- 555-318-4426
We're a professional team of Physical, Occupational, Speech and Therapist Assistants who work together to bring you excellent rehabilitation services. Our knowledge, enthusiasm and drive allow us to be leaders in the healthcare industry.
(Back Cover)
Full Service Contract: We do it all....recruit, employ, teach and audit.
Management Contract: We help you recruit and manage. The manager works for us, the therapists work for you.
Call us for a free audit. 555-318-4426
Industry/Entity Type
Healthcare
Look and feel
Each slider illustrates characteristics of the customer's brand and the style your logo design should communicate.

```html
<!DOCTYPE html>
<html lang="en">
<head>
<meta charset="utf-8">
<title>BrightCove Therapy – Brochure</title>
<link rel="stylesheet" href="https://fonts.googleapis.com/css2?family=Tenor+Sans&family=Open+Sans:wght@400;600;700&display=swap">
<style>
  :root {
    --stage: #5d6b77;
    --paper-top: #ffffff;
    --paper-bottom: #dfe5ec;
    --navy: #2d4a86;
    --navy-deep: #1f3566;
    --gold: #b08a5c;
    --ink: #2a2a2a;
    --ink-soft: #4a4a4a;
    --white: #ffffff;
  }
  * { box-sizing: border-box; margin: 0; padding: 0; }
  html, body {
    width: 1200px; height: 800px; overflow: hidden;
    background: var(--stage);
    font-family: "Open Sans", Arial, sans-serif;
  }
  .brochure { position: relative; width: 1200px; height: 800px; }
  .panel {
    position: absolute; top: 150px; width: 340px; height: 500px;
    background: linear-gradient(180deg, var(--paper-top), var(--paper-bottom) 55%);
    overflow: hidden;
    box-shadow: 0 10px 30px rgba(0,0,0,.3);
  }
  .panel--front { left: 50px; }
  .panel--inside-left { left: 450px; }
  .panel--inside-right { left: 790px; }
  .panel__band { position: absolute; top: 0; left: 0; width: 100%; height: 7px; background: var(--navy); }
  .panel__wave { position: absolute; left: 0; top: 0; width: 100%; height: 100%; }

  .brand { position: absolute; left: 0; width: 100%; text-align: center; }
  .brand__name {
    font-family: "Tenor Sans", Georgia, sans-serif;
    font-size: 29px; color: var(--ink); letter-spacing: .2px;
  }
  .brand__dot {
    display: block; width: 54px; height: 54px; margin: 18px auto 0;
    border-radius: 50%; background: var(--navy);
  }
  .tagline { position: absolute; left: 0; width: 100%; text-align: center; font-family: "Tenor Sans", Georgia, sans-serif; color: var(--ink); }
  .tagline__small { display: block; font-size: 17px; font-weight: 600; }
  .tagline__large { display: block; font-size: 27px; line-height: 1.1; }
  .tagline__rule { display: block; width: 170px; height: 1px; margin: 4px auto 0; background: var(--ink-soft); }

  .front-copy {
    position: absolute; left: 50px; right: 40px; top: 340px;
    color: var(--white); font-weight: 700; font-size: 14px; line-height: 1.45; text-align: center;
  }

  .mission { position: absolute; left: 22px; top: 22px; width: 245px; color: var(--ink); }
  .mission__title { font-family: "Tenor Sans", Georgia, sans-serif; font-size: 20px; font-weight: 600; margin-bottom: 8px; }
  .mission__item { margin-bottom: 8px; }
  .mission__term { font-family: "Tenor Sans", Georgia, sans-serif; font-size: 16px; }
  .mission__desc { font-size: 7.5px; line-height: 1.35; color: var(--ink-soft); }

  .icon-rail {
    position: absolute; right: 12px; top: 30px; width: 34px; height: 230px;
    background: var(--navy); border-radius: 4px;
    display: flex; flex-direction: column; justify-content: space-around; align-items: center;
  }
  .icon-rail svg { width: 20px; height: 20px; }

  .help { position: absolute; left: 18px; top: 355px; color: var(--white); font-weight: 700; }
  .help__title { font-size: 22px; margin-bottom: 10px; }
  .help__list { list-style: none; font-size: 16px; line-height: 1.6; }

  .about {
    position: absolute; left: 24px; right: 24px; top: 345px;
    color: var(--white); font-weight: 600; font-size: 10.5px; line-height: 1.45; text-align: center;
  }
  .contact { position: absolute; left: 0; width: 100%; top: 440px; text-align: center; color: var(--white); font-weight: 700; }
  .contact__web { font-size: 15px; }
  .contact__phone { font-size: 12.5px; margin-top: 2px; }
</style>
</head>
<body>
<main class="brochure">

  <!-- Front cover -->
  <section class="panel panel--front">
    <div class="panel__band"></div>
    <svg class="panel__wave" viewBox="0 0 340 500" preserveAspectRatio="none" aria-hidden="true">
      <path d="M0,222 C70,262 140,300 220,290 S310,276 340,282 L340,500 L0,500 Z" fill="var(--gold)"/>
      <path d="M0,232 C70,272 140,310 220,300 S310,286 340,292 L340,500 L0,500 Z" fill="var(--navy)"/>
    </svg>
    <div class="brand" style="top:52px;">
      <span class="brand__name">BrightCove Therapy</span>
      <span class="brand__dot"></span>
    </div>
    <div class="tagline" style="top:175px;">
      <span class="tagline__small">Keeping You</span>
      <span class="tagline__large">Competitive</span>
      <span class="tagline__rule"></span>
    </div>
    <p class="front-copy">In the ever-changing world of healthcare, you need a partner who can keep you current and ensure you are getting the most out of your rehabilitation services.</p>
  </section>

  <!-- Inside left -->
  <section class="panel panel--inside-left">
    <div class="panel__band"></div>
    <svg class="panel__wave" viewBox="0 0 340 500" preserveAspectRatio="none" aria-hidden="true">
      <path d="M0,330 C70,300 150,272 240,268 S320,262 340,258 L340,500 L0,500 Z" fill="var(--gold)"/>
      <path d="M0,340 C70,310 150,282 240,278 S320,272 340,268 L340,500 L0,500 Z" fill="var(--navy)"/>
    </svg>
    <div class="mission">
      <h2 class="mission__title">Our Mission</h2>
      <div class="mission__item"><div class="mission__term">Quality</div><p class="mission__desc">Recruitment, management, continued education, research and technology</p></div>
      <div class="mission__item"><div class="mission__term">Compliance</div><p class="mission__desc">Accuracy of service within practice guidelines and federal regulations</p></div>
      <div class="mission__item"><div class="mission__term">Expertise</div><p class="mission__desc">Audit and compliance, out-patient, clinical programs, education and career development, evidence based practice and speech and dysphagia programs</p></div>
      <div class="mission__item"><div class="mission__term">Ethics</div><p class="mission__desc">Integrity and social responsibility</p></div>
      <div class="mission__item"><div class="mission__term">Vision</div><p class="mission__desc">To set the standard of performance and practice within the rehabilitation industry</p></div>
    </div>
    <div class="icon-rail" aria-hidden="true">
      <svg viewBox="0 0 20 20"><circle cx="10" cy="10" r="8" fill="none" stroke="#fff" stroke-width="1.5"/><path d="M6 10.5l3 3 5-6" fill="none" stroke="#fff" stroke-width="1.8"/></svg>
      <svg viewBox="0 0 20 20"><path d="M10 2l7 3v5c0 4-3 7-7 8-4-1-7-4-7-8V5z" fill="none" stroke="#fff" stroke-width="1.6"/></svg>
      <svg viewBox="0 0 20 20"><circle cx="10" cy="7" r="4" fill="#fff"/><path d="M3 18c0-4 3-6 7-6s7 2 7 6z" fill="#fff"/></svg>
      <svg viewBox="0 0 20 20"><path d="M10 3v14M5 17h10M3 6h14M3 6l-2 5h4zM17 6l-2 5h4z" fill="none" stroke="#fff" stroke-width="1.4"/></svg>
      <svg viewBox="0 0 20 20"><path d="M1 10c3-5 15-5 18 0-3 5-15 5-18 0z" fill="none" stroke="#fff" stroke-width="1.5"/><circle cx="10" cy="10" r="3" fill="#fff"/></svg>
    </div>
    <div class="help">
      <h3 class="help__title">We're here to help!</h3>
      <ul class="help__list">
        <li>-Improve efficiencies</li>
        <li>-Optimize outcomes</li>
        <li>-Audit for compliance</li>
      </ul>
    </div>
  </section>

  <!-- Inside right -->
  <section class="panel panel--inside-right">
    <div class="panel__band"></div>
    <svg class="panel__wave" viewBox="0 0 340 500" preserveAspectRatio="none" aria-hidden="true">
      <path d="M0,272 C60,300 130,318 200,308 S300,282 340,280 L340,500 L0,500 Z" fill="var(--gold)"/>
      <path d="M0,282 C60,310 130,328 200,318 S300,292 340,290 L340,500 L0,500 Z" fill="var(--navy)"/>
    </svg>
    <div class="brand" style="top:48px;">
      <span class="brand__name">BrightCove Therapy</span>
      <span class="brand__dot"></span>
    </div>
    <div class="tagline" style="top:172px;">
      <span class="tagline__small">Keeping You</span>
      <span class="tagline__large">Competitive</span>
      <span class="tagline__rule"></span>
    </div>
    <p class="about">We're a professional team of Physical, Occupational, Speech and Therapist Assistants who work together to bring you excellent rehabilitation services. Our knowledge, enthusiasm and drive allow us to be leaders in the healthcare industry.</p>
    <div class="contact">
      <div class="contact__web">brightcovetherapy.example</div>
      <div class="contact__phone">Call Us Today- &nbsp;555-318-4426</div>
    </div>
  </section>

</main>
</body>
</html>
```